Project Manager Business Card for Top Architectural Firm

Update and design a stunning Senior Project Manager Business Card

MARCO T. DRUMMOND II
Senior Project Manager

H A L C Y O N
A R C H I T E C T U R E L L C.
www.HalcyonGrandEstates.example
4127 NW 52nd Ter. Suite 2308
Miami, FL 33148
C: (305) 555-0184
mdrummond.halcyongrandestates@mailbox.example

Looking to have the logo to be UV Spot ink printed and to be prominent.

Target Market(s)

High end real estate architecture construction

Industry/Entity Type

Architect

Contact Information for Business Card

MARCO T. DRUMMOND II
Senior Project Manager

H A L C Y O N
Miami, FL 33148
C: (305) 555-0184

Font styles to use
Sans Serif

Colors

Designer to choose colors to be used in the design.

Requirements
Must have
• Prominent Logo

```html
<!DOCTYPE html>
<html lang="en">
<head>
<meta charset="utf-8">
<title>Halcyon Architecture – Business Card</title>
<link rel="stylesheet" href="https://fonts.googleapis.com/css2?family=Montserrat:wght@300;400;500&display=swap">
<style>
  :root {
    --page-bg: #d9e4f1;
    --card-light: #92d6f1;
    --card-mid: #0a8dd0;
    --card-deep: #0680bf;
    --card-dark: #2a5878;
    --ink-dark: #1e1e24;
    --ink-light: #ffffff;
  }
  * { margin: 0; padding: 0; box-sizing: border-box; }
  html, body {
    width: 1200px;
    height: 1000px;
    overflow: hidden;
    background: var(--page-bg);
    font-family: "Montserrat", sans-serif;
  }
  .business-card {
    position: absolute;
    left: 146px;
    top: 242px;
    width: 944px;
    height: 539px;
    border-radius: 32px;
    background: linear-gradient(90deg,
      var(--card-light) 0%,
      var(--card-mid) 47%,
      var(--card-deep) 62%,
      var(--card-dark) 100%);
    overflow: hidden;
  }
  .wordmark {
    position: absolute;
    left: 58px;
    top: 318px;
    width: 290px;
    color: var(--ink-dark);
    font-weight: 500;
    text-align: center;
  }
  .wordmark-name {
    display: block;
    font-size: 54px;
    line-height: 1;
    letter-spacing: 0.2em;
    margin-right: -0.2em;
  }
  .wordmark-sub {
    display: block;
    margin-top: 18px;
    font-size: 15px;
    letter-spacing: 0.28em;
    margin-right: -0.28em;
  }
  .contact-block {
    position: absolute;
    right: 65px;
    top: 118px;
    text-align: right;
    color: var(--ink-light);
  }
  .person-name {
    font-size: 37px;
    font-weight: 500;
    line-height: 44px;
    letter-spacing: 0.01em;
  }
  .person-title {
    font-size: 22px;
    font-weight: 300;
    line-height: 30px;
  }
  .address {
    margin-top: 46px;
    font-size: 23px;
    font-weight: 400;
    line-height: 31px;
    font-style: normal;
  }
  .reach {
    margin-top: 44px;
    font-size: 22px;
    font-weight: 400;
    line-height: 36px;
  }
  .reach .email { font-size: 20px; }
</style>
</head>
<body>
  <section class="business-card">
    <div class="wordmark">
      <span class="wordmark-name">HALCYON</span>
      <span class="wordmark-sub">ARCHITECTURE LLC.</span>
    </div>
    <div class="contact-block">
      <h1 class="person-name">MARCO T. DRUMMOND II</h1>
      <p class="person-title">Senior Project Manager</p>
      <address class="address">
        4127 NW 52nd Ter. Suite 2308<br>
        Miami, FL 33148
      </address>
      <div class="reach">
        <p class="phone">(305) 555-0184</p>
        <p class="website">www.HalcyonGrandEstates.example</p>
        <p class="email">mdrummond.halcyongrandestates@mailbox.example</p>
      </div>
    </div>
  </section>
</body>
</html>
```